Careway Transit private ambulance flyer/broshure

I need a Tri-fold brochure for our BLS non-emergency private ambulance company. We transport patients to doctors appointments, hyperbarics, dialysis, out of town doctors appointment and scheduled medical procedures etc.

```html
<!DOCTYPE html>
<html lang="en">
<head>
<meta charset="utf-8">
<title>Careway Transit – Tri-fold Brochure</title>
<link href="https://fonts.googleapis.com/css2?family=Montserrat:wght@400;500;600;700;800&display=swap" rel="stylesheet">
<style>
:root{
  --navy:#37349a;
  --navy-dark:#2a2780;
  --green:#6cb33f;
  --green-light:#9bd36a;
  --gray-light:#f4f4f4;
  --gray:#cfd0d2;
  --ink:#2b2b33;
  --white:#ffffff;
  --page:#ececec;
}
*{margin:0;padding:0;box-sizing:border-box}
html,body{width:802px;height:1200px;overflow:hidden;background:var(--page);font-family:'Montserrat',sans-serif;color:var(--ink)}
.canvas{position:relative;width:802px;height:1200px}
.spread{position:absolute;left:31px;width:740px;height:572px;overflow:hidden;background:linear-gradient(180deg,var(--gray-light),var(--gray));box-shadow:0 6px 18px rgba(0,0,0,.18)}
.spread--outside{top:20px}
.spread--inside{top:608px}
.spread svg.shapes{position:absolute;inset:0;width:740px;height:572px}
.fold{position:absolute;top:0;bottom:0;width:1px;background:rgba(0,0,0,.08)}
.abs{position:absolute}
.pill{position:absolute;display:inline-block;padding:5px 16px;border-radius:20px;font-weight:700;font-size:14px;letter-spacing:.5px;color:var(--white);background:var(--green);white-space:nowrap}
.pill--navy{background:var(--navy)}
.brand{position:absolute;display:flex;align-items:center;gap:7px;font-weight:800;color:var(--navy);white-space:nowrap}
.brand-dot{width:14px;height:14px;border-radius:50%;background:var(--green)}
.phone-band{position:absolute;color:var(--white);font-weight:600;font-size:15px;letter-spacing:1px;text-align:center}
.bullets{position:absolute;list-style:none;font-size:9.5px;line-height:1.35;color:var(--ink)}
.bullets li{position:relative;padding-left:16px;margin-bottom:9px}
.bullets li::before{content:"";position:absolute;left:0;top:2px;width:6px;height:6px;border-right:2.5px solid var(--navy);border-bottom:2.5px solid var(--navy);transform:rotate(-45deg)}
.contacts{position:absolute;display:grid;grid-template-columns:1fr 1fr;gap:8px 6px;color:var(--white)}
.contact{display:flex;align-items:flex-start;gap:6px}
.contact-icon{flex:none;width:18px;height:18px;border-radius:50%;background:var(--green);display:flex;align-items:center;justify-content:center}
.contact-label{font-weight:700;font-size:11px;line-height:1}
.contact-num{font-size:9px;color:var(--green-light);margin-top:2px}
.body-copy{position:absolute;font-size:8.6px;line-height:1.38;text-align:justify;color:var(--ink)}
.service-list{position:absolute;list-style:none;color:var(--white)}
.service-list li{display:flex;align-items:center;gap:10px;font-size:9.5px;font-weight:500;line-height:1.3;text-transform:uppercase;padding:8px 0;border-bottom:1px solid rgba(255,255,255,.25)}
.service-list li:last-child{border-bottom:none}
.service-icon{flex:none;width:26px;height:26px;border-radius:50%;background:var(--green);display:flex;align-items:center;justify-content:center}
</style>
</head>
<body>
<main class="canvas">

  <!-- OUTSIDE SPREAD -->
  <section class="spread spread--outside" aria-label="Brochure outside">
    <svg class="shapes" viewBox="0 0 740 572" aria-hidden="false">
      <defs>
        <linearGradient id="photoRoad" x1="0" y1="0" x2="1" y2="1">
          <stop offset="0" stop-color="#c9c4bf"/><stop offset=".6" stop-color="#8c8782"/><stop offset="1" stop-color="#5c5a58"/>
        </linearGradient>
        <linearGradient id="photoFleet" x1="0" y1="0" x2="1" y2="1">
          <stop offset="0" stop-color="#e9e6e3"/><stop offset=".55" stop-color="#c98a84"/><stop offset="1" stop-color="#6f6c6a"/>
        </linearGradient>
      </defs>
      <!-- white content area -->
      <path d="M0 70 C200 40 450 30 740 20 L740 460 C560 470 420 420 300 440 C180 460 80 430 0 470 Z" fill="#ffffff"/>
      <!-- top swoosh -->
      <path d="M0 64 C220 30 460 18 740 10" stroke="var(--green)" stroke-width="9" fill="none"/>
      <path d="M0 76 C220 42 460 30 740 22" stroke="var(--navy)" stroke-width="5" fill="none"/>
      <!-- middle navy panel -->
      <path d="M247 45 L494 32 L494 400 C440 410 360 420 300 440 C280 446 262 452 247 456 Z" fill="var(--navy)"/>
      <!-- cover photo -->
      <g role="img" aria-label="Photo of a white ambulance driving on a city road">
        <path d="M494 130 L740 130 L740 330 C660 345 570 360 494 400 Z" fill="url(#photoRoad)"/>
      </g>
      <path d="M494 400 C570 360 660 345 740 330" stroke="var(--navy)" stroke-width="5" fill="none"/>
      <path d="M494 410 C570 370 660 355 740 340" stroke="var(--green)" stroke-width="4" fill="none"/>
      <!-- bottom wave -->
      <path d="M0 470 C80 430 180 460 300 440 C420 420 560 470 740 460" stroke="var(--navy)" stroke-width="6" fill="none"/>
      <path d="M0 484 C80 444 180 474 300 454 C420 434 560 484 740 474" stroke="var(--green)" stroke-width="4" fill="none"/>
      <!-- fleet photo circle -->
      <circle cx="150" cy="545" r="104" fill="var(--navy)"/>
      <g role="img" aria-label="Photo of a row of parked ambulances">
        <circle cx="150" cy="545" r="96" fill="url(#photoFleet)"/>
      </g>
      <!-- green bottom band -->
      <path d="M250 572 C300 530 360 520 420 522 L740 516 L740 572 Z" fill="var(--green)"/>
      <!-- map -->
      <circle cx="370" cy="112" r="58" fill="#ffffff" opacity=".35"/>
      <g role="img" aria-label="Street map showing the office location">
        <circle cx="370" cy="112" r="52" fill="#e8eaee"/>
      </g>
      <path d="M370 98 c-6 0 -10 4 -10 10 c0 8 10 16 10 16 s10 -8 10 -16 c0 -6 -4 -10 -10 -10z" fill="#e53935"/>
      <circle cx="370" cy="108" r="3.5" fill="#ffffff"/>
    </svg>
    <div class="fold" style="left:247px"></div>
    <div class="fold" style="left:494px"></div>

    <!-- Panel 1 -->
    <span class="pill" style="left:32px;top:140px">WE PROVIDE</span>
    <ul class="bullets" style="left:30px;top:182px;width:200px">
      <li>BLS non-emergency private ambulance services,</li>
      <li>Transportation for patients to doctor's appointments, Hyperbaric treatments &amp; Dialysis,</li>
      <li>Out-of-town doctor's appointments,</li>
      <li>Scheduled medical procedures.</li>
    </ul>
    <span class="pill pill--navy" style="left:28px;top:332px;font-size:12px">CAREWAY TRANSIT</span>
    <div class="abs" style="left:50px;top:362px;color:var(--green);font-weight:800;font-size:15px;line-height:1.05">YOUR HEALTH,<br><span style="padding-left:16px">OUR PRIORITY.</span></div>

    <!-- Panel 2 -->
    <p class="abs" style="left:262px;top:190px;width:216px;text-align:center;color:var(--white);font-weight:600;font-size:10.5px;line-height:1.35">FOR MORE INFORMATION ABOUT CAREWAY TRANSIT, PLEASE CONTACT US.</p>
    <span class="pill" style="left:300px;top:240px;font-size:15px">GET IN TOUCH</span>
    <div class="contacts" style="left:268px;top:288px;width:210px">
      <div class="contact"><span class="contact-icon"><svg width="10" height="10" viewBox="0 0 24 24"><path d="M6.6 10.8a15 15 0 006.6 6.6l2.2-2.2a1 1 0 011-.25 11.4 11.4 0 003.6.57 1 1 0 011 1V20a1 1 0 01-1 1A17 17 0 013 4a1 1 0 011-1h3.5a1 1 0 011 1c0 1.25.2 2.45.57 3.6a1 1 0 01-.25 1z" fill="#fff"/></svg></span><div><div class="contact-label">OFFICE</div><div class="contact-num">555-010-4488</div></div></div>
      <div class="contact"><span class="contact-icon"><svg width="10" height="10" viewBox="0 0 24 24"><path d="M6.6 10.8a15 15 0 006.6 6.6l2.2-2.2a1 1 0 011-.25 11.4 11.4 0 003.6.57 1 1 0 011 1V20a1 1 0 01-1 1A17 17 0 013 4a1 1 0 011-1h3.5a1 1 0 011 1c0 1.25.2 2.45.57 3.6a1 1 0 01-.25 1z" fill="#fff"/></svg></span><div><div class="contact-label">FAX</div><div class="contact-num">555-010-4831</div></div></div>
      <div class="contact" style="grid-column:1 / span 2;padding-left:50px"><span class="contact-icon"><svg width="10" height="10" viewBox="0 0 24 24"><path d="M6.6 10.8a15 15 0 006.6 6.6l2.2-2.2a1 1 0 011-.25 11.4 11.4 0 003.6.57 1 1 0 011 1V20a1 1 0 01-1 1A17 17 0 013 4a1 1 0 011-1h3.5a1 1 0 011 1c0 1.25.2 2.45.57 3.6a1 1 0 01-.25 1z" fill="#fff"/></svg></span><div><div class="contact-label">AFTER HOURS</div><div class="contact-num">555-010-4050</div></div></div>
    </div>
    <div class="abs" style="left:300px;top:372px;display:flex;gap:6px;align-items:center;color:var(--white);font-size:7.5px;line-height:1.3">
      <span class="contact-icon" style="width:14px;height:14px"><svg width="8" height="8" viewBox="0 0 24 24"><path d="M12 2a7 7 0 00-7 7c0 5 7 13 7 13s7-8 7-13a7 7 0 00-7-7zm0 9.5A2.5 2.5 0 1112 6.5a2.5 2.5 0 010 5z" fill="#fff"/></svg></span>
      <span>1200 Mesa Verde Rd, Riverton,<br>TX 70000, United States</span>
    </div>
    <div class="brand" style="left:300px;top:470px;font-size:16px"><span class="brand-dot"></span>Careway Transit</div>
    <div class="phone-band" style="left:300px;top:536px;width:194px">555-010-4050</div>

    <!-- Panel 3 -->
    <div class="brand" style="left:530px;top:62px;font-size:20px"><span class="brand-dot"></span>Careway Transit</div>
    <div class="abs" style="left:494px;top:94px;width:246px;text-align:center">
      <div style="color:var(--navy);font-weight:800;font-size:19px;line-height:1.05">NON-EMERGENCY</div>
      <div style="font-weight:700;font-size:11.5px;line-height:1.2">PRIVATE AMBULANCE<br>SERVICES</div>
    </div>
    <div class="abs" style="left:494px;top:408px;width:246px;text-align:center;color:var(--navy);font-weight:800;font-size:24px">BLS &amp; ACLS</div>
    <span class="pill" style="left:516px;top:444px;font-size:11.5px;background:var(--green);color:var(--navy-dark)">TRANSFERS &amp; DISCHARGES</span>
    <div class="phone-band" style="left:494px;top:536px;width:246px">555-010-4488</div>
  </section>

  <!-- INSIDE SPREAD -->
  <section class="spread spread--inside" aria-label="Brochure inside">
    <svg class="shapes" viewBox="0 0 740 572">
      <defs>
        <linearGradient id="photoCrew" x1="0" y1="0" x2="1" y2="1">
          <stop offset="0" stop-color="#dfe7ee"/><stop offset=".5" stop-color="#8fb1cc"/><stop offset="1" stop-color="#c9b1a2"/>
        </linearGradient>
        <linearGradient id="photoCare" x1="0" y1="0" x2="1" y2="1">
          <stop offset="0" stop-color="#efe9e4"/><stop offset=".5" stop-color="#d26a4b"/><stop offset="1" stop-color="#d9d4d0"/>
        </linearGradient>
        <linearGradient id="photoSmall" x1="0" y1="0" x2="1" y2="1">
          <stop offset="0" stop-color="#d8d3d0"/><stop offset=".6" stop-color="#8a6f66"/><stop offset="1" stop-color="#3e4a6a"/>
        </linearGradient>
      </defs>
      <!-- middle navy panel -->
      <rect x="247" y="0" width="247" height="572" fill="var(--navy)"/>
      <!-- panel 1 bottom photo -->
      <g role="img" aria-label="Photo of medical staff in blue scrubs attending a patient">
        <path d="M0 420 C80 400 170 400 247 420 L247 572 L0 572 Z" fill="url(#photoCrew)"/>
      </g>
      <path d="M0 420 C80 400 170 400 247 420" stroke="var(--green)" stroke-width="5" fill="none"/>
      <path d="M0 532 L247 532 L247 572 L0 572 Z" fill="var(--green)"/>
      <circle cx="150" cy="395" r="52" fill="var(--green-light)"/>
      <g role="img" aria-label="Photo of paramedics with a patient on a stretcher">
        <circle cx="150" cy="395" r="45" fill="url(#photoSmall)"/>
      </g>
      <!-- panel 2 circle -->
      <circle cx="370" cy="92" r="68" fill="#5a57b8"/>
      <g role="img" aria-label="Photo of a paramedic caring for a patient on a stretcher">
        <circle cx="370" cy="92" r="60" fill="url(#photoSmall)"/>
      </g>
      <!-- panel 3 top photo -->
      <g role="img" aria-label="Photo of paramedics treating a patient in an ambulance">
        <path d="M494 0 L740 0 L740 170 C650 200 560 210 494 200 Z" fill="url(#photoCare)"/>
      </g>
      <path d="M494 200 C560 210 650 200 740 170" stroke="var(--green)" stroke-width="5" fill="none"/>
      <circle cx="630" cy="178" r="52" fill="var(--green-light)"/>
      <g role="img" aria-label="Photo of a paramedic in a red jacket beside an ambulance">
        <circle cx="630" cy="178" r="45" fill="url(#photoCare)"/>
      </g>
      <path d="M494 500 L740 486 L740 572 L494 572 Z" fill="var(--green)"/>
      <path d="M494 506 L740 492" stroke="var(--green-light)" stroke-width="2"/>
    </svg>
    <div class="fold" style="left:247px"></div>
    <div class="fold" style="left:494px"></div>

    <!-- Panel 1 -->
    <span class="pill" style="left:28px;top:60px">ABOUT US</span>
    <p class="body-copy" style="left:26px;top:100px;width:200px">&rsaquo; At Careway Transit, we are dedicated to providing exceptional healthcare transportation solutions tailored to meet the diverse needs of our clients. With a team of highly trained professionals and a fleet of modern vehicles, we ensure safe, reliable, and comfortable transportation to medical appointments, treatments, and procedures. Our mission is to bridge the gap in access to essential healthcare services, enabling individuals to receive the care they need promptly and conveniently. Whether it's assisting elderly individuals, individuals with disabilities, or those requiring specialized medical care, we are committed to delivering compassionate and personalized service every step of the way. With Careway Transit, you can trust that your healthcare transportation needs are in capable hands.</p>
    <div class="phone-band" style="left:0;top:542px;width:247px">555-010-4488</div>

    <!-- Panel 2 -->
    <span class="pill" style="left:262px;top:178px;font-size:13px">SERVICES WE PROVIDE</span>
    <ul class="service-list" style="left:270px;top:216px;width:205px">
      <li><span class="service-icon"><svg width="14" height="14" viewBox="0 0 24 24"><path d="M3 16V8h11v3h4l3 3v2h-2a2 2 0 01-4 0H9a2 2 0 01-4 0z" fill="#fff"/></svg></span>BLS non-emergency private ambulance services,</li>
      <li><span class="service-icon"><svg width="14" height="14" viewBox="0 0 24 24"><path d="M3 14h18v2H3zm2-4h10v3H5zm1 7a2 2 0 104 0zm8 0a2 2 0 104 0z" fill="#fff"/></svg></span>Transportation for patients to doctor's appointments, hyperbaric treatments, dialysis</li>
      <li><span class="service-icon"><svg width="14" height="14" viewBox="0 0 24 24"><path d="M6 3a3 3 0 013 3c0 2-3 5-3 5S3 8 3 6a3 3 0 013-3zm12 10a3 3 0 013 3c0 2-3 5-3 5s-3-3-3-5a3 3 0 013-3zM6 13h6a2 2 0 010 4H9" stroke="#fff" stroke-width="1.6" fill="none"/></svg></span>Out-of-town doctor's appointments,</li>
      <li><span class="service-icon"><svg width="14" height="14" viewBox="0 0 24 24"><path d="M12 20s-8-5-8-11a4.5 4.5 0 018-2.8A4.5 4.5 0 0120 9c0 6-8 11-8 11z" fill="#fff"/></svg></span>Scheduled medical procedures.</li>
    </ul>
    <div class="abs" style="left:262px;top:430px;width:216px;text-align:center;color:var(--green);font-weight:800;font-size:14px">GET IN TOUCH</div>
    <div class="contacts" style="left:268px;top:452px;width:210px">
      <div class="contact"><span class="contact-icon"><svg width="10" height="10" viewBox="0 0 24 24"><path d="M6.6 10.8a15 15 0 006.6 6.6l2.2-2.2a1 1 0 011-.25 11.4 11.4 0 003.6.57 1 1 0 011 1V20a1 1 0 01-1 1A17 17 0 013 4a1 1 0 011-1h3.5a1 1 0 011 1c0 1.25.2 2.45.57 3.6a1 1 0 01-.25 1z" fill="#fff"/></svg></span><div><div class="contact-label">OFFICE</div><div class="contact-num">555-010-4488</div></div></div>
      <div class="contact"><span class="contact-icon"><svg width="10" height="10" viewBox="0 0 24 24"><path d="M6.6 10.8a15 15 0 006.6 6.6l2.2-2.2a1 1 0 011-.25 11.4 11.4 0 003.6.57 1 1 0 011 1V20a1 1 0 01-1 1A17 17 0 013 4a1 1 0 011-1h3.5a1 1 0 011 1c0 1.25.2 2.45.57 3.6a1 1 0 01-.25 1z" fill="#fff"/></svg></span><div><div class="contact-label">FAX</div><div class="contact-num">555-010-4831</div></div></div>
      <div class="contact" style="grid-column:1 / span 2;padding-left:50px"><span class="contact-icon"><svg width="10" height="10" viewBox="0 0 24 24"><path d="M6.6 10.8a15 15 0 006.6 6.6l2.2-2.2a1 1 0 011-.25 11.4 11.4 0 003.6.57 1 1 0 011 1V20a1 1 0 01-1 1A17 17 0 013 4a1 1 0 011-1h3.5a1 1 0 011 1c0 1.25.2 2.45.57 3.6a1 1 0 01-.25 1z" fill="#fff"/></svg></span><div><div class="contact-label">AFTER HOURS</div><div class="contact-num">555-010-4050</div></div></div>
    </div>
    <div class="phone-band" style="left:247px;top:542px;width:247px">555-010-4050</div>

    <!-- Panel 3 -->
    <span class="pill" style="left:512px;top:252px">WHY CHOOSE US</span>
    <p class="body-copy" style="left:512px;top:292px;width:210px">&rsaquo; Careway Transit is dedicated to offering comprehensive and compassionate healthcare transportation solutions, tailored to meet the diverse needs of our clients, including elderly individuals, individuals with disabilities, and those requiring specialized medical care, thereby bridging the gap in access to vital healthcare services by providing safe, reliable, and punctual transportation to medical appointments, treatments, and procedures, ultimately contributing to improved health outcomes and quality of life for our clients and their families.</p>
    <div class="phone-band" style="left:494px;top:530px;width:246px">555-010-4488</div>
  </section>

</main>
</body>
</html>
```